Business acrd and Stationery desgin FOR HARLOW

I want creative and expressive stationary design .on the front side for business card I need the logo and doctors name to be there and on the back side I need time and appointment .Please see attached business card to use same names ,but use address below and phone number

Note:the deigner must submit the file in vector format and PSD and PDF

Business name is :Harlow Crest Medical Clinic.

Address:
20485 57 ST NW
City :EDMONTON AB
Postal code: T6K 3P8

Phone :(780) 492-3815
Fax:(780) 492-5127

Other Business name :Harlow Medical Clinic

• logo in the back on business card

```html
<!DOCTYPE html>
<html lang="en">
<head>
<meta charset="utf-8">
<title>Harlow Crest Medical Clinic – Business Card</title>
<link href="https://fonts.googleapis.com/css2?family=Montserrat:wght@600;700&family=Questrial&display=swap" rel="stylesheet">
<style>
  :root {
    --bg: #e9eaec;
    --card: #fbfbfa;
    --navy: #24337f;
    --red: #c8191f;
    --ink: #3a3a3a;
    --rule: #6a6a6a;
  }
  * { box-sizing: border-box; margin: 0; padding: 0; }
  html, body { width: 1200px; height: 1000px; overflow: hidden; }
  body { background: var(--bg); position: relative; font-family: "Questrial", sans-serif; }

  .card {
    position: absolute; left: 338px; width: 530px; height: 303px;
    background: var(--card);
    box-shadow: 0 2px 6px rgba(0,0,0,.18);
    overflow: hidden;
  }
  .card--front { top: 163px; }
  .card--back { top: 549px; }

  .band-top { position: absolute; top: 0; left: 0; right: 0; height: 7px; background: var(--red); }
  .band-bottom { position: absolute; bottom: 0; left: 0; right: 0; height: 10px; background: var(--navy); }

  .doctors {
    position: absolute; left: 34px; top: 55px;
    font-family: "Montserrat", sans-serif; font-weight: 700;
    font-size: 15px; line-height: 21px; color: var(--navy);
  }

  .brand {
    position: absolute; display: flex; align-items: center; gap: 10px;
    font-family: "Montserrat", sans-serif; font-weight: 600;
    font-size: 16px; line-height: 19px; letter-spacing: .5px;
  }
  .brand__dot { width: 26px; height: 26px; border-radius: 50%; flex: none; }
  .card--front .brand { right: 34px; top: 54px; color: var(--navy); }
  .card--front .brand__dot { background: var(--red); }

  .services {
    position: absolute; left: 34px; top: 229px;
    font-family: "Montserrat", sans-serif; font-weight: 700;
    font-size: 12.5px; line-height: 16px; color: var(--navy);
  }
  .services .lead { color: var(--red); }

  .address {
    position: absolute; right: 167px; top: 239px;
    text-align: right; font-size: 13px; line-height: 19.5px; color: var(--ink);
  }
  .contact {
    position: absolute; left: 390px; top: 239px;
    font-size: 13px; line-height: 19.5px; color: var(--ink);
  }
  .contact li { list-style: none; display: flex; align-items: center; gap: 7px; }
  .contact svg { width: 13px; height: 13px; flex: none; }

  .header {
    position: absolute; top: 0; left: 0; right: 0; height: 114px; background: var(--navy);
  }
  .card--back .brand { left: 37px; top: 36px; color: #ffffff; }
  .card--back .brand__dot { background: var(--red); }
  .header__title {
    position: absolute; left: 362px; top: 45px;
    font-family: "Montserrat", sans-serif; font-weight: 700;
    font-size: 12.5px; color: #ffffff; letter-spacing: .2px;
  }

  .appointments { position: absolute; left: 37px; top: 155px; width: 458px; list-style: none; }
  .appointment {
    display: flex; align-items: flex-end; height: 35px;
    font-size: 13px; color: var(--ink);
  }
  .appointment__num { width: 16px; }
  .blank { display: inline-block; border-bottom: 1px solid var(--rule); height: 13px; }
  .blank--time { width: 18px; margin-left: 2px; }
  .blank--note { flex: 1; margin: 0 4px 0 4px; }
  .blank--d { width: 30px; }
  .blank--m { width: 20px; }
  .blank--y { width: 26px; }
  .slash { margin: 0 1px; }
</style>
</head>
<body>

<section class="card card--front" aria-label="Business card front">
  <div class="band-top"></div>

  <div class="doctors">
    <p>Dr N OKAFOR</p>
    <p>Dr L VASQUEZ</p>
  </div>

  <div class="brand">
    <span class="brand__dot"></span>
    <span>HARLOW CREST<br>MEDICAL CLINIC</span>
  </div>

  <div class="services">
    <p class="lead">Family Doctors</p>
    <p>Family Practice</p>
    <p>&amp; walk in welcome</p>
  </div>

  <address class="address" style="font-style:normal">
    20485 57 ST NW<br>
    Edmonton AB, T6K 3P8
  </address>

  <ul class="contact">
    <li>
      <svg viewBox="0 0 13 13" aria-hidden="true">
        <rect width="13" height="13" rx="2" fill="#c8191f"/>
        <path d="M4 3.2c.5-.3.9-.2 1.1.2l.6 1.2c.2.4 0 .7-.3.9l-.3.2c.3.9 1 1.6 1.9 2l.2-.3c.2-.3.6-.4.9-.2l1.2.6c.4.2.5.6.2 1.1-.4.7-1.1 1-1.9.7C5.6 9.2 3.8 7.4 3.3 5.4c-.2-.8.1-1.6.7-2.2z" fill="#fff"/>
      </svg>
      (780) 492-3815
    </li>
    <li>
      <svg viewBox="0 0 13 13" aria-hidden="true">
        <rect width="13" height="13" rx="2" fill="#c8191f"/>
        <rect x="4" y="2.5" width="5" height="3" fill="#fff"/>
        <rect x="2.5" y="5.5" width="8" height="4" rx="1" fill="#fff"/>
        <rect x="4" y="8.5" width="5" height="2.5" fill="#fff" stroke="#c8191f" stroke-width=".6"/>
      </svg>
      (780) 492-5127
    </li>
  </ul>

  <div class="band-bottom"></div>
</section>

<section class="card card--back" aria-label="Business card back">
  <div class="header">
    <div class="brand">
      <span class="brand__dot"></span>
      <span>HARLOW CREST<br>MEDICAL CLINIC</span>
    </div>
    <h2 class="header__title">YOUR APPOINTMENTS</h2>
  </div>

  <ol class="appointments">
    <li class="appointment"><span class="appointment__num">1.</span><span class="blank blank--time"></span>am/pm<span class="blank blank--note"></span><span class="blank blank--d"></span><span class="slash">/</span><span class="blank blank--m"></span><span class="slash">/</span><span class="blank blank--y"></span></li>
    <li class="appointment"><span class="appointment__num">2.</span><span class="blank blank--time"></span>am/pm<span class="blank blank--note"></span><span class="blank blank--d"></span><span class="slash">/</span><span class="blank blank--m"></span><span class="slash">/</span><span class="blank blank--y"></span></li>
    <li class="appointment"><span class="appointment__num">3.</span><span class="blank blank--time"></span>am/pm<span class="blank blank--note"></span><span class="blank blank--d"></span><span class="slash">/</span><span class="blank blank--m"></span><span class="slash">/</span><span class="blank blank--y"></span></li>
    <li class="appointment"><span class="appointment__num">4.</span><span class="blank blank--time"></span>am/pm<span class="blank blank--note"></span><span class="blank blank--d"></span><span class="slash">/</span><span class="blank blank--m"></span><span class="slash">/</span><span class="blank blank--y"></span></li>
  </ol>
</section>

</body>
</html>
```